VELQUARTH - A modern gin bottle label

Design of a bottle label in a modern fresh design. The name of the gin is "VELQUARTH Hollow Batch K7". Please take a look at the velquarth.de website. on the main page of velquarth.de you can breathe the design direction here: 1) the taste of the gin should be composed of 10 botanicals ... an important scent note. ) a distinctive flavor is spicy and fresh 3.) The filling volume is 0.5 liters 4.) the alcohol content is 43% vol. 5.) the variety is called "dry gin" 6.) velquarth stands for "energy" and "love"

Target Market(s)

Alcohol consumer

Colors

Designer to choose colors to be used in the design.

Requirements
Must have
• the velquarth corporate logo must be included, the name of the gin is "VELQUARTH Hollow Batch K7"
Nice to have
• Please use the bottles template in the appendix. (The Black Bottles) they can use the saying "DESTILLED & BOTTLED BY OLD MARROW" in small letters

```html
<!DOCTYPE html>
<html lang="en">
<head>
<meta charset="utf-8">
<title>VELQUARTH Hollow Batch K7 – Label</title>
<link rel="stylesheet" href="https://fonts.googleapis.com/css2?family=Anton&family=Montserrat:wght@600&family=Saira+Condensed:wght@700&family=Saira:wght@800&family=Gochi+Hand&display=swap">
<style>
  :root {
    --page: #f4f4f2;
    --label-dark: #0c0b10;
    --label-night: #1f1b2c;
    --moon: #3a2a1c;
    --moon-glow: rgba(160, 90, 30, 0.35);
    --title-green: #9cc52a;
    --ink-white: #f2f2f2;
    --ink-muted: #b9b6c2;
  }
  * { margin: 0; padding: 0; box-sizing: border-box; }
  html, body {
    width: 1200px; height: 1200px; overflow: hidden;
    background: var(--page);
  }
  .canvas { position: relative; width: 1200px; height: 1200px; }

  .label {
    position: absolute; left: 260px; top: 100px;
    width: 680px; height: 1000px;
    background: linear-gradient(180deg, var(--label-dark) 0%, var(--label-night) 55%, var(--label-dark) 100%);
    overflow: hidden;
  }

  .moon {
    position: absolute; left: 190px; top: 29px;
    width: 300px; height: 300px; border-radius: 50%;
    background: radial-gradient(circle, var(--moon) 0%, rgba(40,28,20,0.8) 55%, rgba(20,16,20,0) 72%);
    box-shadow: 0 0 60px var(--moon-glow);
  }

  .brand-name {
    position: absolute; left: 0; right: 0; top: 152px;
    text-align: center;
    font-family: "Montserrat", sans-serif; font-weight: 600;
    font-size: 38px; letter-spacing: 5px;
    color: var(--ink-white);
  }

  .graveyard-scene {
    position: absolute; left: 0; top: 342px;
    width: 680px; height: 300px;
  }

  .variety {
    position: absolute; right: 48px; top: 588px;
    font-family: "Saira Condensed", sans-serif; font-weight: 700;
    font-size: 40px; line-height: 1; letter-spacing: 3px;
    color: var(--ink-white);
  }

  .product-name {
    position: absolute; left: 0; right: 0; top: 648px;
    text-align: center;
    font-family: "Anton", sans-serif;
    font-size: 180px; line-height: 1;
    letter-spacing: 4px;
    color: var(--title-green);
  }

  .batch {
    position: absolute; left: 0; right: 0; top: 852px;
    text-align: center;
    font-family: "Saira", sans-serif; font-weight: 800;
    font-size: 46px; line-height: 1; letter-spacing: 7px;
    color: var(--ink-white);
  }

  .facts {
    position: absolute; left: 12px; right: 12px; top: 935px;
    display: flex; justify-content: space-between; align-items: center;
  }
  .facts .volume, .facts .strength {
    font-family: "Saira Condensed", sans-serif; font-weight: 700;
    font-size: 30px; color: var(--ink-white);
  }
  .facts .maker {
    font-family: "Gochi Hand", cursive;
    font-size: 19px; letter-spacing: 1px;
    color: var(--ink-muted);
    transform: translateY(-12px);
  }
</style>
</head>
<body>
<main class="canvas">
  <section class="label">
    <div class="moon"></div>
    <div class="brand-name">VELQUARTH</div>

    <svg class="graveyard-scene" role="img" aria-label="Illustration of a night graveyard with crosses, tombstones, flying bats and a zombie climbing out of the ground" viewBox="0 0 680 300" preserveAspectRatio="none">
      <defs>
        <linearGradient id="scene-fill" x1="0" y1="0" x2="0" y2="1">
          <stop offset="0" stop-color="#1c1826" stop-opacity="0"/>
          <stop offset="0.4" stop-color="#2a2438"/>
          <stop offset="1" stop-color="#14121a"/>
        </linearGradient>
      </defs>
      <rect width="680" height="300" fill="url(#scene-fill)"/>
    </svg>

    <div class="variety">DRY GIN</div>
    <div class="product-name">HOLLOW</div>
    <div class="batch">BATCH K7</div>

    <div class="facts">
      <span class="volume">0.5 L</span>
      <span class="maker">DESTILLED &amp; BOTTLED BY OLD MARROW</span>
      <span class="strength">43% VOL</span>
    </div>
  </section>
</main>
</body>
</html>
```